I need a newspaper ads that suits events / outings all over the world. refreshing feeling that suits my company logo.
Size of the ads is 6cm by 6cm a square
takenote
1) Joining up as members is free .
2) Places of interest tickets discount for members
3) Special events / outings host almost everyday
4) main point is everyone able to know each another
website : www.WanderNookly.com
Target Market(s)
Targeting general age 18-40 . mainly singles
contents to put inside the ads
2) Local Places of interest tickets discount for members
4) Website : www.WanderNookly.com
5) We also host photos contest
6) Meet the different faces of the world
7) Experience Sharing Gathering !
Industry/Entity Type
It Company
Requirements
Must have
- Refreshing feeling , and professional . will be uploading more pictures , kindly put some pictures combine into it to make people feel there is a lot activities can be involve when they join as member.

```html
<!DOCTYPE html>
<html lang="en">
<head>
<meta charset="utf-8">
<title>NovaGlobe Events – Members Ad</title>
<link rel="stylesheet" href="https://fonts.googleapis.com/css2?family=Arimo:wght@700&family=Roboto+Condensed:wght@400;700&display=swap">
<style>
  :root {
    --paper: #f8f5ec;
    --ink: #353535;
    --orange: #f39a1e;
    --orange-deep: #ef8a1a;
    --purple: #7e6cb0;
    --green: #7cbc42;
    --cyan: #1ab6e0;
    --navy: #1f4a8a;
    --footer-dark: #0b2548;
    --footer-mid: #12467a;
    --footer-line: #7fd3f2;
    --white: #ffffff;
  }
  * { margin: 0; padding: 0; box-sizing: border-box; }
  html, body { width: 1200px; height: 1200px; overflow: hidden; }
  body { background: var(--paper); position: relative; font-family: "Arimo", Arial, sans-serif; }

  .hero { position: absolute; left: 0; top: 0; width: 1200px; height: 600px; }

  .brand {
    position: absolute; right: 40px; top: 22px; width: 250px;
    display: flex; flex-direction: column; align-items: center;
    color: var(--navy); font-family: "Arimo", Arial, sans-serif; font-weight: 700;
  }
  .brand-dot { width: 92px; height: 92px; border-radius: 50%; background: var(--navy); margin-bottom: 14px; }
  .brand-name { font-size: 38px; line-height: 1; letter-spacing: 1px; }
  .brand-sub { font-size: 30px; line-height: 1.1; letter-spacing: 8px; margin-top: 2px; }

  .headline {
    position: absolute; top: 588px; left: 0; width: 1200px; text-align: center;
    font-size: 52px; color: var(--ink); font-weight: 700; letter-spacing: -0.5px;
  }
  .tagline {
    position: absolute; top: 658px; left: 0; width: 1200px; text-align: center;
    font-size: 47px; font-weight: 700;
  }
  .tag-experience { color: var(--orange-deep); }
  .tag-sharing { color: var(--purple); }
  .tag-gathering { color: var(--green); }

  .perk {
    position: absolute; height: 73px; display: flex; align-items: center; justify-content: center;
    color: var(--white); font-family: "Roboto Condensed", "Arial Narrow", sans-serif;
    font-size: 45px; font-weight: 400;
  }
  .perk::before, .perk::after {
    content: ""; position: absolute; top: 50%; width: 26px; height: 26px; margin-top: -13px;
    border-radius: 50%; background: var(--white);
  }
  .perk::before { left: 26px; }
  .perk::after { right: 26px; }
  .perk-free { left: 220px; width: 757px; top: 735px; background: var(--orange); }
  .perk-tickets { left: 14px; width: 1172px; top: 831px; background: var(--cyan); }
  .perk-events { left: 42px; width: 1116px; top: 924px; background: var(--green); }
  .perk-contest { left: 220px; width: 757px; top: 1014px; background: var(--purple); }

  .contact-bar {
    position: absolute; left: 0; bottom: 0; width: 1200px; height: 93px;
    background: linear-gradient(90deg, var(--footer-dark), var(--footer-mid) 50%, var(--footer-dark));
    border-top: 5px solid var(--footer-line);
    display: flex; align-items: center; justify-content: center;
    color: var(--white); font-family: "Roboto Condensed", "Arial Narrow", sans-serif;
    font-weight: 700; font-size: 52px; letter-spacing: 3px;
  }
</style>
</head>
<body>
  <svg class="hero" width="1200" height="600" viewBox="0 0 1200 600">
    <defs>
      <linearGradient id="groupPhotoTone" x1="0" y1="0" x2="1" y2="1">
        <stop offset="0" stop-color="#4f5a4c"/>
        <stop offset="0.45" stop-color="#6f6a5e"/>
        <stop offset="1" stop-color="#3c3a3a"/>
      </linearGradient>
    </defs>
    <polyline points="0,130 785,130 888,222 1200,222" fill="none" stroke="#f39a1e" stroke-width="12"/>
    <path d="M0,142 L780,142 L880,234 L1200,234 L1200,566 L0,566 Z" fill="url(#groupPhotoTone)"
          role="img" aria-label="Photo of a smiling group of six young friends on an outing"/>
    <rect x="0" y="566" width="1200" height="10" fill="#f39a1e"/>
  </svg>

  <div class="brand">
    <span class="brand-dot"></span>
    <span class="brand-name">NOVAGLOBE</span>
    <span class="brand-sub">EVENTS</span>
  </div>

  <h1 class="headline">Meet the different faces of the world</h1>
  <p class="tagline">
    <span class="tag-experience">Experience</span>
    <span class="tag-sharing">Sharing</span>
    <span class="tag-gathering">Gathering !</span>
  </p>

  <div class="perk perk-free">Joining up as members is free</div>
  <div class="perk perk-tickets">Local Places of interest tickets discount for members</div>
  <div class="perk perk-events">Special events / outings host almost everyday</div>
  <div class="perk perk-contest">We also host photos contest</div>

  <div class="contact-bar">Call: 01987654320 | www.WanderNookly.com</div>
</body>
</html>
```